I want a website to be designed for our new company, it's an import and export company for variety of things.

please see the attached Logo for our company and the Images for our different sections for our busienss

Target Market(s)

multiple

Coding

Coded - Design and coding required

Number of Pages Required

5+ page

Font styles to use
Sans Serif

Colors

Designer to choose colors to be used in the design.

Requirements
Must have
• KDR WORLDWIDE
• KDR worlwide Supply & Building provides various services. The Company offers infrastructure construction, oil, enegy and gas services, agricultural projects, real estate development, travel and tourism, and food processing and trading.
• Civil contracting for infrastructure, residential and heavy projects. Through its main subsidiaries; distribution of general food products, construction chemicals including corrosion inhibitors and electrical machinery; provides catering and travel agency services; ownership and operation of a school; offers human sources services including manpower supply.
• Drilling and Gold Mines Used Machinery, All Kinds of Construction Machinery, Drilling Machines are manufactured and sold.
Nice to have
• good designa and beautiful colours, it has too look professional

```html
<!DOCTYPE html>
<html lang="en">
<head>
<meta charset="utf-8">
<title>KDR WORLDWIDE</title>
<link rel="stylesheet" href="https://fonts.googleapis.com/css2?family=Poppins:ital,wght@0,400;0,500;0,600;0,700;1,500&family=Roboto:wght@400;500&display=swap">
<style>
:root{
  --red:#ee1c25;
  --red-dark:#c8101a;
  --ink:#111111;
  --text:#333333;
  --muted:#777777;
  --light:#f7f7f7;
  --footer:#1b1b1b;
  --white:#ffffff;
  --blob:#f1f4fa;
  --blue:#1f6fe0;
}
*{box-sizing:border-box;margin:0;padding:0}
html,body{width:1200px;height:3125px;overflow:hidden;background:var(--white)}
body{position:relative;font-family:"Poppins",sans-serif;color:var(--ink)}
.abs{position:absolute}
.center{text-align:center}

/* header */
.site-header{position:absolute;left:0;top:0;width:1200px;height:87px;background:var(--white)}
.nav-link{position:absolute;top:45px;font-size:15px;font-weight:500;color:var(--ink)}
.nav-link.active{color:var(--red)}
.brand-box{position:absolute;left:521px;top:0;width:158px;height:134px;background:#1a1a1a;z-index:3;display:flex;align-items:center;justify-content:center;flex-direction:column}
.brand-name{font-family:"Poppins",sans-serif;font-weight:500;font-size:14px;letter-spacing:1px;color:var(--white);text-align:center;line-height:1.3}
.contact-link{position:absolute;top:43px;font-size:12.5px;font-weight:500;color:var(--red)}

/* hero */
.hero{position:absolute;left:0;top:87px;width:1200px;height:554px;background:linear-gradient(180deg,#2d64b8 0%,#4b82cc 30%,#6f5c5a 55%,#8a3b2c 75%,#1f3e6e 100%)}
.hero-band{position:absolute;left:0;top:197px;width:1200px;height:162px;background:rgba(60,66,78,.72)}
.hero-title{position:absolute;left:0;top:230px;width:1200px;text-align:center;color:var(--white);font-weight:700;font-size:40px;line-height:47px;letter-spacing:.3px}
.hero-arrow{position:absolute;top:259px;width:36px;height:36px}

/* services */
.eyebrow{position:absolute;left:0;width:1200px;text-align:center;color:var(--red);font-size:17px;font-weight:400}
.section-title{position:absolute;left:0;width:1200px;text-align:center;font-weight:700;color:var(--ink)}
.lead{position:absolute;left:0;width:1200px;text-align:center;font-size:13.5px;line-height:15px;color:var(--ink)}
.service-card{position:absolute;top:881px;width:261px;height:359px;background:var(--white);box-shadow:0 4px 12px rgba(0,0,0,.28)}
.service-photo{position:absolute;left:0;top:0;width:261px;height:185px}
.service-icon{position:absolute;left:95px;top:150px;width:70px;height:70px;border-radius:50%;background:var(--red);border:3px solid var(--white);display:flex;align-items:center;justify-content:center}
.service-name{position:absolute;left:0;top:224px;width:100%;text-align:center;color:var(--red);font-size:20px;font-weight:600}
.service-text{position:absolute;left:12px;top:262px;width:237px;text-align:center;font-family:"Roboto",sans-serif;font-size:12.5px;line-height:13.5px;color:var(--ink)}
.read-btn{position:absolute;left:77px;top:343px;width:108px;height:35px;background:var(--red);color:var(--white);font-family:"Roboto",sans-serif;font-size:12px;display:flex;align-items:center;justify-content:center}
.round-arrow{position:absolute;width:36px;height:36px}
.dot{position:absolute;top:1293px;width:12px;height:12px;border-radius:50%;border:2px solid var(--red)}
.dot.on{background:var(--red)}

/* why us */
.why{position:absolute;left:0;top:1369px;width:1200px;height:400px;background:var(--light)}
.why-photo{position:absolute;left:139px;top:76px;width:294px;height:268px;background:linear-gradient(135deg,#d7e2ee 0%,#8ea6c0 45%,#2f3d52 100%)}
.why-title{position:absolute;left:457px;top:72px;font-size:30px;font-weight:700;color:var(--ink)}
.why-title span{color:var(--red)}
.why-text{position:absolute;left:457px;width:305px;font-family:"Roboto",sans-serif;font-size:11.5px;line-height:19px;color:#444}
.why-more{position:absolute;left:457px;top:333px;font-family:"Roboto",sans-serif;font-size:11px;color:var(--red)}
.why-rule{position:absolute;left:774px;top:76px;width:2px;height:268px;background:var(--red)}
.feature{position:absolute;left:804px;display:flex;align-items:center;gap:16px}
.feature-icon{width:42px;height:42px;border-radius:50%;background:var(--red);display:flex;align-items:center;justify-content:center}
.feature-label{font-family:"Roboto",sans-serif;font-size:15.5px;letter-spacing:.6px;color:var(--ink)}

/* quote */
.quote{position:absolute;left:0;top:1769px;width:1200px;height:458px}
.quote-left{position:absolute;left:0;top:0;width:607px;height:458px;background:linear-gradient(135deg,#e52532 0%,#d21c2a 55%,#b51520 100%)}
.quote-photo{position:absolute;left:607px;top:0;width:593px;height:458px;background:linear-gradient(160deg,#9aa39a 0%,#c3b89c 45%,#e2e3e6 70%,#6e6d66 100%)}
.quote-title{position:absolute;left:235px;top:45px;font-size:20px;font-weight:500;color:var(--white);letter-spacing:.3px}
.quote-sub{position:absolute;left:235px;top:80px;font-size:8.5px;font-weight:600;letter-spacing:4.5px;color:var(--white)}
.field{position:absolute;height:29px;background:var(--white);font-family:"Roboto",sans-serif;font-size:8.5px;color:#777;padding:10px 0 0 15px;letter-spacing:.3px}
.quote-btn{position:absolute;left:235px;top:372px;width:141px;height:34px;background:var(--red);color:var(--white);font-family:"Roboto",sans-serif;font-size:10.5px;font-weight:500;display:flex;align-items:center;justify-content:center}

/* testimonials */
.tcard{position:absolute;top:2371px;width:357px;height:360px;border-radius:50%;background:var(--blob)}
.avatar-ring{position:absolute;left:0;top:0;width:124px;height:124px;border-radius:50%;border:3px dashed var(--blue);display:flex;align-items:center;justify-content:center}
.avatar{width:104px;height:104px;border-radius:50%;background:linear-gradient(160deg,#c9b7a7,#6d5647)}
.tname{position:absolute;left:151px;top:54px;font-size:16.5px;font-weight:600;color:#1b1b2a}
.trole{position:absolute;left:151px;top:79px;font-size:10px;color:#8a8aa0}
.stars{position:absolute;left:151px;top:95px;font-size:9px;color:#f28c1c;letter-spacing:3px}
.tquote{position:absolute;left:42px;top:158px;width:290px;font-size:10.5px;font-style:italic;font-weight:500;line-height:17px;color:#1b1b2a}
.tbody{position:absolute;left:42px;top:202px;width:290px;font-size:9.5px;line-height:17.5px;color:#8a8aa0}
.socials{position:absolute;left:112px;top:287px;display:flex;gap:11px}
.social{width:24px;height:24px;border-radius:50%;border:1px solid #b8c0d8;background:var(--white)}
.social.on{background:var(--blue);border-color:var(--blue)}
.pager{position:absolute;top:2732px;width:26px;height:26px;border-radius:50%;border:1px solid #b8c0d8}

/* footer */
.site-footer{position:absolute;left:0;top:2779px;width:1200px;height:346px;background:var(--footer);color:var(--white)}
.footer-brand{position:absolute;left:240px;top:62px;font-size:14px;font-weight:500;letter-spacing:1px}
.footer-text{position:absolute;left:240px;width:165px;font-family:"Roboto",sans-serif;font-size:8.5px;line-height:12.5px;color:#cfcfcf}
.footer-contact{position:absolute;left:240px;font-family:"Roboto",sans-serif;font-size:8.5px;color:var(--red)}
.footer-head{position:absolute;top:104px;font-size:13.5px;font-weight:500;letter-spacing:.3px}
.footer-head::after{content:"";position:absolute;left:0;bottom:-5px;width:26px;height:2px;background:var(--red)}
.footer-links{position:absolute;top:150px;list-style:none;font-family:"Roboto",sans-serif;font-size:8.5px;color:#cfcfcf}
.footer-links li{height:23px}
.footer-links li::before{content:"›";margin-right:6px;color:#cfcfcf}
.hours{position:absolute;left:804px;width:171px;font-family:"Roboto",sans-serif;font-size:8.5px;color:#cfcfcf;display:flex;justify-content:space-between;padding-bottom:8px;border-bottom:1px dashed #444}
.subscribe{position:absolute;left:804px;top:227px;width:137px;height:31px;background:#2b2b2b;font-family:"Roboto",sans-serif;font-size:8.5px;color:#aaa;padding:11px 0 0 9px}
.subscribe-btn{position:absolute;left:941px;top:227px;width:33px;height:31px;background:var(--red);display:flex;align-items:center;justify-content:center}
</style>
</head>
<body>

<header class="site-header">
  <a class="nav-link active" style="left:92px">Home</a>
  <a class="nav-link" style="left:183px">Services</a>
  <a class="nav-link" style="left:273px">About Us</a>
  <a class="nav-link" style="left:386px">Contact Us</a>
  <div class="brand-box"><div class="brand-name">KDR<br>WORLDWIDE</div></div>
  <span class="contact-link" style="left:715px">Email@kdrworldwide.com</span>
  <span class="contact-link" style="left:944px">|</span>
  <span class="contact-link" style="left:988px">410-5550-1290</span>
</header>

<section class="hero" role="img" aria-label="Cargo ship loaded with containers at port, with a passenger jet flying overhead">
  <div class="hero-band"></div>
  <h1 class="hero-title">KDR WORLDWIDE YOUR TRUSTED<br>PARTNER IN EXPORT AND IMPORT</h1>
  <svg class="hero-arrow" style="left:33px" viewBox="0 0 36 36"><circle cx="18" cy="18" r="16" fill="none" stroke="#fff" stroke-width="2.5"/><path d="M21 11l-7 7 7 7" fill="none" stroke="#fff" stroke-width="3"/></svg>
  <svg class="hero-arrow" style="left:1111px" viewBox="0 0 36 36"><circle cx="18" cy="18" r="16" fill="none" stroke="#fff" stroke-width="2.5"/><path d="M15 11l7 7-7 7" fill="none" stroke="#fff" stroke-width="3"/></svg>
</section>

<p class="eyebrow" style="top:696px">Our Services</p>
<h2 class="section-title" style="top:726px;font-size:29px;line-height:35px">KDR worlwide Supply &amp; Building<br>provides various services</h2>
<p class="lead" style="top:807px">The Company offers infrastructure construction, oil, enegy and gas services, agricultural projects,<br>real estate development, travel and tourism, and food processing and trading.</p>

<svg class="round-arrow" style="left:73px;top:1030px" viewBox="0 0 36 36"><circle cx="18" cy="18" r="16" fill="none" stroke="#ee1c25" stroke-width="2.5"/><path d="M21 11l-7 7 7 7" fill="none" stroke="#ee1c25" stroke-width="3"/></svg>
<svg class="round-arrow" style="left:1088px;top:1030px" viewBox="0 0 36 36"><circle cx="18" cy="18" r="16" fill="none" stroke="#ee1c25" stroke-width="2.5"/><path d="M15 11l7 7-7 7" fill="none" stroke="#ee1c25" stroke-width="3"/></svg>

<article class="service-card" style="left:177px">
  <div class="service-photo" role="img" aria-label="Offshore oil rig at sea" style="background:linear-gradient(180deg,#9fb5c2,#3e6a7a 60%,#2c4f5c)"></div>
  <div class="service-icon"><svg width="26" height="30" viewBox="0 0 26 30"><path d="M13 2C9 10 5 14 5 19a8 8 0 0016 0c0-5-4-9-8-17z" fill="#fff"/></svg></div>
  <h3 class="service-name">Oil and Gas</h3>
  <p class="service-text">Lorem Ipsum Lorem Ipsum Lorem Ipsum Lorem Ipsum Lorem Ipsum Lorem Ipsum Lorem Ipsum Lorem Ipsum Lorem Ipsum Lorem Ipsum</p>
  <span class="read-btn">Read More</span>
</article>
<article class="service-card" style="left:475px">
  <div class="service-photo" role="img" aria-label="Aerial view of a large building complex" style="background:linear-gradient(180deg,#c9cfd3,#8f9a9d 60%,#5c6a5e)"></div>
  <div class="service-icon"><svg width="30" height="30" viewBox="0 0 30 30"><rect x="5" y="6" width="10" height="20" fill="#fff"/><rect x="16" y="12" width="9" height="14" fill="#fff"/><rect x="8" y="9" width="2" height="3" fill="#ee1c25"/><rect x="11" y="9" width="2" height="3" fill="#ee1c25"/><rect x="8" y="15" width="2" height="3" fill="#ee1c25"/><rect x="11" y="15" width="2" height="3" fill="#ee1c25"/></svg></div>
  <h3 class="service-name">Building</h3>
  <p class="service-text">Lorem Ipsum Lorem Ipsum Lorem Ipsum Lorem Ipsum Lorem Ipsum Lorem Ipsum Lorem Ipsum Lorem Ipsum Lorem Ipsum Lorem Ipsum</p>
  <span class="read-btn">Read More</span>
</article>
<article class="service-card" style="left:770px">
  <div class="service-photo" role="img" aria-label="Yellow drilling machine in a snowy forest" style="background:linear-gradient(180deg,#aab6bd,#7d8a86 50%,#d9dde0)"></div>
  <div class="service-icon"><svg width="32" height="28" viewBox="0 0 32 28"><path d="M4 20h22v4H4z" fill="#fff"/><path d="M8 20V12h8l4 8z" fill="#fff"/><path d="M18 12l8-8 3 3-7 7" fill="none" stroke="#fff" stroke-width="3"/></svg></div>
  <h3 class="service-name">Business &amp; Machines</h3>
  <p class="service-text">Lorem Ipsum Lorem Ipsum Lorem Ipsum Lorem Ipsum Lorem Ipsum Lorem Ipsum Lorem Ipsum Lorem Ipsum Lorem Ipsum Lorem Ipsum</p>
  <span class="read-btn">Read More</span>
</article>

<span class="dot on" style="left:575px"></span>
<span class="dot" style="left:594px"></span>
<span class="dot" style="left:614px"></span>

<section class="why">
  <div class="why-photo" role="img" aria-label="Two business people shaking hands over documents"></div>
  <h2 class="why-title"><span>Why</span> Choose Us?</h2>
  <p class="why-text" style="top:124px">Contrary to popular belief, Lorem Ipsum is not simply random text. It has roots in a piece of classical Latin literature from 45 BC, making</p>
  <p class="why-text" style="top:201px">All the Lorem Ipsum generators on the Internet tend to repeat predefined chunks as necessary, making this the first true generator on the Internet. It uses a dictionary of over 200 Latin words, combined with a handful of model sentence structures, to generate Lorem Ipsum which looks reasonable.</p>
  <span class="why-more">READ MORE &nbsp;›</span>
  <div class="why-rule"></div>
  <div class="feature" style="top:98px"><span class="feature-icon"><svg width="22" height="16" viewBox="0 0 22 16"><path d="M2 8l5-5 4 3 4-3 5 5-7 6z" fill="none" stroke="#fff" stroke-width="2"/></svg></span><span class="feature-label">WE ARE TRUSTED</span></div>
  <div class="feature" style="top:158px"><span class="feature-icon"><svg width="16" height="20" viewBox="0 0 16 20"><rect x="2" y="9" width="12" height="10" rx="1" fill="#fff"/><path d="M5 9V5a4 4 0 018 0" fill="none" stroke="#fff" stroke-width="2"/></svg></span><span class="feature-label">THE BEST SEQURITY</span></div>
  <div class="feature" style="top:218px"><span class="feature-icon"><svg width="20" height="20" viewBox="0 0 20 20"><path d="M2 9h4v9H2zM7 9l4-7c2 0 2 2 1.5 4H18l-2 12H7z" fill="none" stroke="#fff" stroke-width="2"/></svg></span><span class="feature-label">100% GUARANTEE</span></div>
  <div class="feature" style="top:278px"><span class="feature-icon"><svg width="22" height="18" viewBox="0 0 22 18"><ellipse cx="9" cy="7" rx="7" ry="5" fill="none" stroke="#fff" stroke-width="2"/><path d="M5 11l-2 4 5-3M14 9c4 0 6 2 6 4l1 3-4-2" fill="none" stroke="#fff" stroke-width="2"/></svg></span><span class="feature-label">24/7 SUPPORT</span></div>
</section>

<section class="quote">
  <div class="quote-left" role="img" aria-label="Red-tinted airport apron with service truck"></div>
  <div class="quote-photo" role="img" aria-label="Passenger aircraft at the gate with catering truck and ground service vehicles"></div>
  <h2 class="quote-title">GET A FREE QUOTE</h2>
  <p class="quote-sub">WE ALWAYS USE BEST &amp; FASTEST FLEETS</p>
  <div class="field" style="left:235px;top:112px;width:364px">FULL NAME</div>
  <div class="field" style="left:235px;top:152px;width:172px">EMAIL</div>
  <div class="field" style="left:426px;top:152px;width:173px">MOBILE</div>
  <div class="field" style="left:235px;top:191px;width:172px">DESTINATION FROM</div>
  <div class="field" style="left:426px;top:191px;width:173px">DESTINATION TO</div>
  <div class="field" style="left:235px;top:230px;width:172px">SHIPPING TYPE</div>
  <div class="field" style="left:426px;top:230px;width:173px">SHIPPING DATE</div>
  <div class="field" style="left:235px;top:270px;width:364px;height:89px">MESSAGE</div>
  <span class="quote-btn">SEND US QUOTE</span>
</section>

<p class="eyebrow" style="top:2265px;font-size:13px">Testimonial</p>
<h2 class="section-title" style="top:2293px;font-size:19px;line-height:23px;font-weight:600">WHAT PEOPLE SAY<br>ABOUT OUR SERVICES</h2>

<article class="tcard" style="left:231px">
  <div class="avatar-ring"><div class="avatar" role="img" aria-label="Portrait photo of a client"></div></div>
  <h3 class="tname">Lena Moreau</h3>
  <p class="trole">Marketing Officer</p>
  <p class="stars">★★★★★</p>
  <p class="tquote">Ut enim minim veniam quis nostrud exercitation ullam commodo consequat sint sunt in culpa.</p>
  <p class="tbody">Ut enim ad minim veniam, quis nostrud exercitation ullamco commodo consequat is aute irure in reprehenderit voluptat proident, sunt in culpa qui officia deserunt Ut enim minim irure in reprehenderit voluptat.</p>
  <div class="socials"><span class="social"></span><span class="social on"></span><span class="social"></span><span class="social"></span></div>
</article>
<article class="tcard" style="left:607px">
  <div class="avatar-ring"><div class="avatar" role="img" aria-label="Portrait photo of a client"></div></div>
  <h3 class="tname">Mira Okafor</h3>
  <p class="trole">Marketing Officer</p>
  <p class="stars">★★★★★</p>
  <p class="tquote">Ut enim minim veniam quis nostrud exercitation ullam commodo consequat sint sunt in culpa.</p>
  <p class="tbody">Ut enim ad minim veniam, quis nostrud exercitation ullamco commodo consequat is aute irure in reprehenderit voluptat proident, sunt in culpa qui officia deserunt Ut enim minim irure in reprehenderit voluptat.</p>
  <div class="socials"><span class="social"></span><span class="social on"></span><span class="social"></span><span class="social"></span></div>
</article>
<svg class="pager" style="left:565px" viewBox="0 0 26 26"><path d="M17 13H9m3-3l-3 3 3 3" fill="none" stroke="#8a8aa0" stroke-width="1.2"/></svg>
<svg class="pager" style="left:603px" viewBox="0 0 26 26"><path d="M9 13h8m-3-3l3 3-3 3" fill="none" stroke="#8a8aa0" stroke-width="1.2"/></svg>

<footer class="site-footer">
  <div class="footer-brand">KDR WORLDWIDE</div>
  <p class="footer-text" style="top:155px">It was popularised in the 1960s with the release of Letraset sheets containing Lorem Ipsum passages.</p>
  <p class="footer-text" style="top:202px">It was popularised in the 1960s with the release of Letraset sheets containing Lorem Ipsum passages.</p>
  <p class="footer-contact" style="top:253px">☎ &nbsp;+00 0100 555 201</p>
  <p class="footer-contact" style="top:272px">✉ &nbsp;info@kdrworldwide.com</p>
  <p class="footer-contact" style="top:291px">☏ &nbsp;+00 02 555 789</p>

  <h4 class="footer-head" style="left:492px">QUICK LINKS</h4>
  <ul class="footer-links" style="left:492px">
    <li>Company Overview</li><li>Aspiration &amp; Vision</li><li>Quality Policy</li><li>Press Ad</li><li>Brochure</li><li>Latest News</li><li>Media Gallery</li>
  </ul>
  <h4 class="footer-head" style="left:679px">USEFULL LINKS</h4>
  <ul class="footer-links" style="left:679px">
    <li>Company Overview</li><li>Aspiration &amp; Vision</li><li>Quality Policy</li><li>Press Ad</li><li>Brochure</li><li>Latest News</li><li>Media Gallery</li>
  </ul>
  <h4 class="footer-head" style="left:866px">OPENING HOURS</h4>
  <div class="hours" style="left:866px;top:150px;width:168px"><span>Sat to Thurs:</span><span>09:30AM to 05:30PM</span></div>
  <div class="hours" style="left:866px;top:182px;width:168px"><span>Fri:</span><span>Closed</span></div>
  <div class="subscribe" style="left:866px">Enter your email</div>
  <span class="subscribe-btn" style="left:1003px"><svg width="16" height="16" viewBox="0 0 16 16"><path d="M1 8l14-6-5 13-2-5z" fill="#fff"/></svg></span>
</footer>

</body>
</html>
```